Stationary Design needed for luxorious bespoke tailor

We need a design for our stationary items like businescards, letters, envelope and letter head / Signature for email. Our company "LE CORVAN" sells exclusively and luxourious bespoke garments and accessories for men. The desgins of letterhead, envelope and business card shoulderstand communicate luxury, high quality and good taste. We would like our logo to be used on the designs.

Target Market(s)

Gentleman with a high aproach and exclusive and luxourious suits and shirts, grooms, businesman,

Industry/Entity Type

It Company

Font styles to use
Sans Serif

Colors
ec1f27
ffffff

Requirements
Must have
• Logo, Companies name and adress, contactName internet & email, phone number line / mobile, VAT Nr. On Business Card frontpage only logo and name, adress companies on backpage. No VAT and Companies ID there. Company data; LE CORVAN AG Wiesenrain 42 4057 Basel Switzerland VAT: CHE 472 916 304 Tax Tel 41 61 594 17 36 Mobile 41 79 842 06 91 www.korvanmode.ch info@korvanmode.com.
Nice to have
• -Name And phone numbers need to be able to change (for different coworkers ...)
Should not have
• no VAT in Business Card

```html
<!DOCTYPE html>
<html lang="de">
<head>
<meta charset="utf-8">
<title>LE CORVAN – E-Mail-Signatur</title>
<link href="https://fonts.googleapis.com/css2?family=Montserrat:wght@500;600&family=Didact+Gothic&display=swap" rel="stylesheet">
<style>
  :root {
    --ink: #231f20;
    --ink-soft: #3a3a3a;
    --accent: #ec1f27;
    --paper: #ffffff;
    --rule: #bdbdbd;
  }
  html, body {
    margin: 0;
    padding: 0;
    width: 1200px;
    height: 991px;
    overflow: hidden;
    background: var(--paper);
  }
  .signature {
    position: absolute;
    left: 150px;
    top: 330px;
    width: 900px;
    color: var(--ink);
    font-family: "Didact Gothic", "Century Gothic", sans-serif;
  }
  .person-name {
    margin: 0;
    font-family: "Montserrat", sans-serif;
    font-weight: 600;
    font-size: 25px;
    letter-spacing: 0.5px;
  }
  .person-role {
    margin: 2px 0 0;
    font-size: 27px;
    color: var(--ink-soft);
  }
  .details {
    display: flex;
    align-items: center;
    margin-top: 42px;
  }
  .contact-list,
  .address-list {
    margin: 0;
    padding: 0;
    list-style: none;
    font-size: 19px;
    line-height: 24px;
    color: var(--ink-soft);
  }
  .contact-list li {
    display: flex;
    align-items: center;
    gap: 8px;
  }
  .contact-icon {
    width: 18px;
    height: 18px;
    flex: none;
  }
  .divider {
    width: 1px;
    height: 72px;
    background: var(--rule);
    margin: 0 30px;
  }
  .brand-name {
    margin: 0 0 0 4px;
    font-family: "Montserrat", sans-serif;
    font-weight: 600;
    font-size: 54px;
    letter-spacing: 3px;
    color: var(--ink);
  }
</style>
</head>
<body>
  <section class="signature">
    <h1 class="person-name">ELIAS BRUNNER</h1>
    <p class="person-role">Manager</p>

    <div class="details">
      <ul class="contact-list">
        <li>
          <svg class="contact-icon" viewBox="0 0 18 18" aria-hidden="true">
            <rect width="18" height="18" rx="2" fill="var(--accent)"/>
            <path d="M5 4h3l1 3-1.5 1a7 7 0 0 0 2.5 2.5L11 9l3 1v3a1 1 0 0 1-1 1A9 9 0 0 1 4 5a1 1 0 0 1 1-1z" fill="#fff"/>
          </svg>
          +41 61 594 17 36
        </li>
        <li>
          <svg class="contact-icon" viewBox="0 0 18 18" aria-hidden="true">
            <rect width="18" height="18" rx="2" fill="var(--accent)"/>
            <rect x="3.5" y="5" width="11" height="8" fill="none" stroke="#fff" stroke-width="1.4"/>
            <path d="M3.5 5l5.5 4.5L14.5 5" fill="none" stroke="#fff" stroke-width="1.4"/>
          </svg>
          info@korvanmode.ch
        </li>
        <li>
          <svg class="contact-icon" viewBox="0 0 18 18" aria-hidden="true">
            <rect width="18" height="18" rx="2" fill="var(--accent)"/>
            <circle cx="9" cy="9" r="5.5" fill="none" stroke="#fff" stroke-width="1.3"/>
            <ellipse cx="9" cy="9" rx="2.4" ry="5.5" fill="none" stroke="#fff" stroke-width="1.1"/>
            <path d="M3.5 9h11" stroke="#fff" stroke-width="1.1"/>
          </svg>
          www.korvanmode.ch
        </li>
      </ul>

      <span class="divider"></span>

      <ul class="address-list">
        <li>Wiesenrain 42</li>
        <li>4057 Basel, Switzerland</li>
        <li>VAT: CHE-472.916.304 MwSt</li>
      </ul>

      <span class="divider"></span>

      <p class="brand-name">LE CORVAN</p>
    </div>
  </section>
</body>
</html>
```